依頼詳細
■デザインのみになります。コーディング・設置は必要ありません。

ターゲットの方々が経営者や弁護士・医師の方々ですので、シックな雰囲気や高級感のあるテイストを希望しています。あまりごちゃごちゃしない方がいいです。そしてPC表示とスマートフォン表示は別のものを用意していただきたいと思っています。その辺りは以下のサイトを参照してください。

https://ka-gakuin.example/lp1/

ファッション系のサービスなので、デザインにも、そこそここだわりたいと思っています。指標となるデザインは以下を参照してください。このようなテイストが個人的に好みです。あくまで参考程度に。

https://www.verdalune.example/
https://www.shokumalink.example/user/landing/general01
https://shigoto-meijin.example/

それではみなさんからのご提案を楽しみにしております。どうぞ宜しくお願いいたします。※デザインのみになります。コーディングは必要ありません。
サイトURL
http://kiriharada.example/
ページ数
5ページ
希望イメージ
シンプル 複雑
単色 カラフル
暗い 明るい
日常 高級
遊び心 厳粛
未来的 伝統的
女性的 男性的
希望する色
青系、茶系、グレー系
納品ファイル
• フォトショップ形式 (.psd)
• PNG形式 (.png)
補足説明
・ホームページとスマートフォンでデザインが最適化されることを望んでいます。
・原稿は「添付ファイル」を参照してください。
・写真素材はこちらからダウンロードをお願いします。
http://22.filebako.example/0617-x7k29d41m3p8q05r6t2w9y4z8c1v7n3b5
■LPは縦長の1ページでお願いします
■文章量は添付ファイルをご確認ください
■ページ数が5ページとなっていますが、制作は縦長の1ページでお願いします。それなりに文章量がありますので、5ページという形で表現しています。
写真素材は以下からダウンロードしてください。http://26.filebako.example/0624-h4j8l2n6p0r3t7v1x5z9b2d6f0g4k8m1q(ギガファイル便6月24日まで)
■ 選んだ理由

センスの良さが際立っていました。ファッション分野のLPなので、細部にまで満足のいくデザインに巡り会えたのはとてもありがたいことだと感じています。

■ 提案者全員のお礼・コメント

この度は優れたデサインを多数ご提案いただきまして、誠にありがとうございました。レベルが高く、選ぶのが大変でしたがとても満足のいくコンペになりました。また機会がありましたら宜しくお願いいたします。

```html
<!DOCTYPE html>
<html lang="ja">
<head>
<meta charset="utf-8">
<title>KA styling | 経営者のための専属スタイリストサービス</title>
<link rel="stylesheet" href="https://fonts.googleapis.com/css2?family=Noto+Serif+JP:wght@400;600;700&family=Noto+Sans+JP:wght@400;500;700&family=Cormorant+Garamond:wght@500;600&display=swap">
<style>
:root{
  --ink:#2a2a2a;
  --ink-soft:#555;
  --dark:#2c2b2a;
  --dark-2:#3a3836;
  --paper:#ffffff;
  --paper-2:#f6f4f1;
  --gold:#e59a3c;
  --gold-soft:#f6d19a;
  --cream:#fbe6c4;
  --teal:#2fa39b;
  --line:#cfc8bf;
}
*{margin:0;padding:0;box-sizing:border-box}
html,body{width:1200px;height:4416px;overflow:hidden}
body{font-family:"Noto Sans JP",sans-serif;color:var(--ink);background:var(--paper);position:relative}
.serif{font-family:"Noto Serif JP",serif}
.en{font-family:"Cormorant Garamond",serif;letter-spacing:.3em}

/* HERO */
.hero{position:absolute;left:0;top:0;width:1200px;height:760px;
  background:linear-gradient(100deg,#f2efe9 0%,#d8d1c6 28%,#6d5a48 55%,#3a2c22 80%,#2a211b 100%)}
.hero-photo{position:absolute;inset:0;background:radial-gradient(ellipse at 70% 35%,rgba(190,140,80,.45),transparent 55%),radial-gradient(ellipse at 90% 80%,rgba(20,15,12,.7),transparent 60%)}
.brand{position:absolute;left:110px;top:62px;display:flex;align-items:center;gap:16px;color:#fff}
.brand-mark{width:46px;height:46px;border:2px solid #fff;border-radius:50%}
.brand-name{font-family:"Noto Serif JP",serif;font-size:34px;font-weight:600}
.brand-sub{position:absolute;left:172px;top:104px;font-size:12px;color:#fff;letter-spacing:.3em}
.hero-lead{position:absolute;left:110px;top:262px;font-size:24px;font-weight:700;color:#2a2a2a;background:rgba(255,255,255,.85);padding:8px 18px}
.hero-lead em{font-style:normal;color:var(--gold);font-size:30px}
.hero-title{position:absolute;left:110px;top:340px;font-family:"Noto Serif JP",serif;color:#fff;font-size:56px;font-weight:600;line-height:1.4;letter-spacing:.12em;text-shadow:0 2px 10px rgba(0,0,0,.35)}

.cta{position:absolute;display:flex;align-items:center;height:96px}
.cta-badge{width:96px;height:116px;background:var(--dark);color:#fff;text-align:center;font-size:14px;padding-top:12px;line-height:1.3;margin-top:-10px}
.cta-badge b{display:block;font-family:"Noto Serif JP",serif;font-size:44px;color:var(--gold-soft);line-height:1.1}
.cta-body{height:96px;width:480px;background:linear-gradient(90deg,var(--cream),var(--gold-soft));display:flex;align-items:center;justify-content:space-between;padding:0 30px 0 36px;font-family:"Noto Serif JP",serif;font-size:30px;font-weight:700;line-height:1.3;color:var(--ink)}
.cta-body svg{flex:none}

/* PROFILE */
.profile{position:absolute;left:0;top:690px;width:1200px;height:760px;background:var(--paper);clip-path:polygon(0 70px,1200px 0,1200px 690px,0 760px)}
.sec-label{position:absolute;font-family:"Cormorant Garamond",serif;font-weight:600;font-size:30px;letter-spacing:.3em}
.profile .sec-label{left:120px;top:140px}
.profile .sec-label::after{content:"";position:absolute;left:0;top:50px;width:60px;height:2px;background:var(--ink)}
.prof-title{position:absolute;left:120px;top:240px;font-size:22px;font-weight:500}
.prof-name{position:absolute;left:120px;top:290px;font-family:"Noto Serif JP",serif;font-size:46px;font-weight:700;letter-spacing:.15em}
.prof-name-en{position:absolute;left:122px;top:360px;font-size:12px;letter-spacing:.35em;color:var(--ink-soft)}
.prof-media{position:absolute;left:120px;top:400px;font-size:16px;line-height:1.9;width:560px}
.books{position:absolute;left:120px;top:500px;display:flex;gap:32px}
.book{width:130px;height:150px}
.stylist-photo{position:absolute;left:690px;top:40px;width:420px;height:660px;background:linear-gradient(180deg,#f0ece6,#c9b9a6 40%,#2d3a52 70%,#8a5a35 100%)}

/* PROBLEMS */
.problems{position:absolute;left:0;top:1380px;width:1200px;height:1230px;background:linear-gradient(180deg,var(--dark),var(--dark-2));clip-path:polygon(0 70px,1200px 0,1200px 1160px,0 1230px)}
.problems .sec-label{left:0;width:1200px;text-align:center;top:120px;color:#fff}
.problems .sec-label::after{content:"";position:absolute;left:570px;top:54px;width:60px;height:2px;background:#fff}
.prob-q{position:absolute;left:0;width:1200px;text-align:center;top:240px;color:#fff;font-size:26px;font-weight:500;letter-spacing:.06em}
.prob-q::after{content:"";display:block;width:640px;height:1px;background:rgba(255,255,255,.5);margin:16px auto 0}
.checks{position:absolute;left:300px;top:330px;list-style:none}
.checks li{display:flex;align-items:center;gap:22px;color:#fff;font-size:22px;height:64px}
.tick{width:32px;height:32px;background:var(--teal);display:flex;align-items:center;justify-content:center}
.prob-foot{position:absolute;left:0;width:1200px;top:1010px;text-align:center;color:#fff;font-size:24px}
.prob-foot b{color:var(--gold);font-size:48px;font-family:"Noto Serif JP",serif;vertical-align:-6px}
.bulb{position:absolute;left:570px;top:1090px}

/* PURPOSE */
.purpose .sec-label{left:0;width:1200px;text-align:center;top:2690px;color:var(--ink)}
.purpose-line{position:absolute;left:570px;top:2744px;width:60px;height:2px;background:var(--ink)}
.purpose-head{position:absolute;left:0;width:1200px;top:2800px;text-align:center;font-family:"Noto Serif JP",serif;font-size:34px;font-weight:700;letter-spacing:.08em}
.purpose-text{position:absolute;left:230px;width:740px;font-size:16px;line-height:2;text-align:center;color:var(--ink-soft)}
.purpose-text b{color:var(--gold)}
.reason-photo{position:absolute}
.reason-card{position:absolute;background:var(--paper);padding:40px 40px;box-shadow:0 6px 24px rgba(0,0,0,.12)}
.reason-card h3{font-family:"Noto Serif JP",serif;font-size:26px;line-height:1.5;border-left:4px solid var(--gold);padding-left:18px;margin-bottom:22px}
.reason-card p{font-size:15px;line-height:2;color:var(--ink-soft)}
.bg-soft{position:absolute;left:0;top:3430px;width:1200px;height:986px;background:var(--paper-2)}
</style>
</head>
<body>

<header class="hero">
  <div class="hero-photo" role="img" aria-label="落ち着いたセレクトショップの店内、暖色の照明とスーツが並ぶ棚"></div>
  <div class="brand"><span class="brand-mark"></span><span class="brand-name">KA styling</span></div>
  <div class="brand-sub">KAKU STYLING</div>
  <p class="hero-lead serif">既に<em>100</em>名以上が<em>センスのいい経営者</em>に変わった</p>
  <h1 class="hero-title">経営者のための<br>専属スタイリストサービス</h1>
  <a class="cta" style="left:110px;top:512px">
    <span class="cta-badge">毎日<b>3</b>名限定</span>
    <span class="cta-body">初回カウンセリングの<br>お申込みはこちら
      <svg width="26" height="40" viewBox="0 0 26 40"><path d="M4 4l14 16-14 16M12 4l14 16-14 16" fill="none" stroke="#e59a3c" stroke-width="3"/></svg>
    </span>
  </a>
</header>

<section class="profile">
  <h2 class="sec-label">PROFILE</h2>
  <p class="prof-title">累計5万部以上の著書を持つスタイリスト</p>
  <p class="prof-name">桐原 遥</p>
  <p class="prof-name-en">KIRIHARA HARUKA</p>
  <p class="prof-media">「あさひかりテレビ」（みなとテレビ）「おはよう朝便」（中央放送）<br>「経済日報」「週刊セレクト」（青葉書房）などメディア出演多数</p>
  <div class="books">
    <div class="book" role="img" aria-label="著書の表紙（濃紺）" style="background:#1f2d4a"></div>
    <div class="book" role="img" aria-label="著書の表紙（白と紺）" style="background:linear-gradient(#eef0f3,#3b5a86)"></div>
    <div class="book" role="img" aria-label="著書の表紙（水色）" style="background:#bcd7e8"></div>
    <div class="book" role="img" aria-label="著書の表紙（ネイビーのジャケット）" style="background:linear-gradient(#f2f2f2,#27385a)"></div>
  </div>
  <div class="stylist-photo" role="img" aria-label="ネイビーのジャケットを着て木製の脚立に腰掛けるスタイリスト"></div>
</section>

<section class="problems">
  <h2 class="sec-label">PROBLEMS</h2>
  <p class="prob-q">日々のファッションにこんな悩みはありませんか？</p>
  <ul class="checks">
    <li><span class="tick"><svg width="20" height="16"><path d="M2 8l6 6L18 2" fill="none" stroke="#fff" stroke-width="3"/></svg></span>ビジネスでのブランディングに力を入れたい</li>
    <li><span class="tick"><svg width="20" height="16"><path d="M2 8l6 6L18 2" fill="none" stroke="#fff" stroke-width="3"/></svg></span>講演やセミナーなどで人前に立つことが増えてきた</li>
    <li><span class="tick"><svg width="20" height="16"><path d="M2 8l6 6L18 2" fill="none" stroke="#fff" stroke-width="3"/></svg></span>メディアに出演することが増えてきた</li>
    <li><span class="tick"><svg width="20" height="16"><path d="M2 8l6 6L18 2" fill="none" stroke="#fff" stroke-width="3"/></svg></span>今の立場にふさわしいファッションに変わりたい</li>
    <li><span class="tick"><svg width="20" height="16"><path d="M2 8l6 6L18 2" fill="none" stroke="#fff" stroke-width="3"/></svg></span>信頼される見た目に変わりたい</li>
    <li><span class="tick"><svg width="20" height="16"><path d="M2 8l6 6L18 2" fill="none" stroke="#fff" stroke-width="3"/></svg></span>自分のセンスに自信がない</li>
    <li><span class="tick"><svg width="20" height="16"><path d="M2 8l6 6L18 2" fill="none" stroke="#fff" stroke-width="3"/></svg></span>服選びは奥さんや店員さんに任せっぱなし</li>
    <li><span class="tick"><svg width="20" height="16"><path d="M2 8l6 6L18 2" fill="none" stroke="#fff" stroke-width="3"/></svg></span>いつまでも魅力的な経営者でありたい</li>
  </ul>
  <p class="prob-foot"><b>1</b>つでも当てはまる方は日々のファッションを見直してみてください。</p>
  <svg class="bulb" width="60" height="70" viewBox="0 0 60 70"><circle cx="30" cy="28" r="18" fill="#f6d19a"/><rect x="22" y="48" width="16" height="10" fill="#fff"/><path d="M30 2v4M6 28h4M50 28h4M12 10l3 3M48 10l-3 3" stroke="#fff" stroke-width="2"/></svg>
</section>

<section class="purpose">
  <div class="bg-soft"></div>
  <h2 class="sec-label">PURPOSE</h2>
  <span class="purpose-line"></span>
  <p class="purpose-head">優秀な経営者がファッションに気を配る理由とは？</p>
  <p class="purpose-text" style="top:2880px">近年、ファッションに気を配る経営者が増えています。それなぜ専属のサービスを利用してまで、服装を整える必要があるのか。その答えをここでお伝えしていきます。</p>
  <p class="purpose-text" style="top:2980px">それはご自身の価値を正しく伝えるためであり、ファッションを<b>ビジネスツール</b>として捉えているからです。</p>

  <div class="reason-photo" role="img" aria-label="街並みを背景にスーツと蝶ネクタイ姿で立つ男性" style="left:520px;top:3080px;width:580px;height:460px;background:linear-gradient(135deg,#c9b79c,#7d8a9a 50%,#2a2f3a)"></div>
  <div class="reason-card" style="left:100px;top:3170px;width:500px">
    <h3>他社との差別化に<br>パーソナルブランディングは不可欠</h3>
    <p>企業間競争が激しい今、経営者自身の印象が会社の評価を左右します。装いを整えることは、最も手軽で効果の高いブランディングです。</p>
    <p>第一印象は数秒で決まるといわれます。信頼を得る見た目づくりを、専門家と一緒に始めましょう。</p>
  </div>

  <div class="reason-photo" role="img" aria-label="スーツの袖口と腕時計を整える男性の手元" style="left:100px;top:3620px;width:580px;height:400px;background:linear-gradient(135deg,#3a3a3a,#1d1d1d 60%,#6b6258)"></div>
  <div class="reason-card" style="left:600px;top:3690px;width:500px">
    <h3>最短距離で<br>「センスのいい経営者」になる方法とは？</h3>
    <p>忙しい経営者が自分で服を選ぶには時間も労力もかかります。プロに任せることで、最短で理想の装いを手に入れることができます。</p>
    <p>専属スタイリストが体型や立場、目指す印象に合わせて一人ひとりに最適なスタイルをご提案します。</p>
  </div>

  <a class="cta" style="left:360px;top:4150px">
    <span class="cta-badge">毎日<b>3</b>名限定</span>
    <span class="cta-body">初回カウンセリングの<br>お申込みはこちら
      <svg width="26" height="40" viewBox="0 0 26 40"><path d="M4 4l14 16-14 16M12 4l14 16-14 16" fill="none" stroke="#e59a3c" stroke-width="3"/></svg>
    </span>
  </a>
</section>

</body>
</html>
```